Poster design for a vet clinic

Running a campaign called 'Tail teller', which is where people get a $30 voucher for themselves and their friend if they refer somebody to our vet clinic.

Text something like:
We love Tail Tellers!
Refer a fur friend to our friendly team and both your fur child and their fur child will receive a $30 voucher to use in clinic! *
* Limited to one pet per fur parent and the referred fur parent must be new to our clinic. Unlimited vouchers for number of referrals!

I want it to be cute but professional. You can see the design styles at mossbury-vet.com.au/kelvale and see the logo there too.
I am thinking of having a dog whispering to a cat or something like that as the main image.
I would like both the photoshop file and the pdf please. Would be for an A2 poster.

```html
<!DOCTYPE html>
<html lang="en">
<head>
<meta charset="utf-8">
<title>We Love Tail Tellers – Mossbury Vet Clinic</title>
<link href="https://fonts.googleapis.com/css2?family=Montserrat:wght@700;800&family=Oleo+Script:wght@700&family=Fira+Sans+Condensed:wght@700&family=Arvo:wght@400;700&family=PT+Sans+Narrow:wght@700&family=Roboto+Slab:wght@500&display=swap" rel="stylesheet">
<style>
  :root {
    --paper: #f3f1ec;
    --brown: #6b4a3a;
    --orange: #f0861f;
    --orange-deep: #e77817;
    --yellow-light: #fdc923;
    --yellow-deep: #f7a81d;
    --teal: #1a9fa6;
    --ink: #1f1a17;
    --white: #ffffff;
  }
  html, body { margin: 0; padding: 0; overflow: hidden; background: var(--paper); }
  .poster {
    position: relative;
    width: 846px;
    height: 1200px;
    overflow: hidden;
    background: var(--paper);
    font-family: "Arvo", serif;
  }
  .hero-photo {
    position: absolute;
    left: 0; top: 0;
    width: 846px; height: 380px;
    background:
      radial-gradient(ellipse 200px 170px at 330px 220px, #d99a4f 0%, rgba(217,154,79,0) 100%),
      radial-gradient(ellipse 170px 170px at 640px 180px, #cbbfb4 0%, rgba(203,191,180,0) 100%),
      linear-gradient(#ffffff, #f7f4ef);
  }
  .torn-edge { position: absolute; left: 0; top: 318px; }

  .voucher-badge { position: absolute; left: 14px; top: 22px; }
  .voucher-frame {
    position: absolute; left: 14px; top: 28px;
    width: 282px; height: 106px;
    border: 2px solid var(--ink);
    transform: rotate(-9deg);
  }
  .voucher-tag {
    position: absolute; left: 26px; top: 46px;
    width: 268px; height: 84px;
    background: var(--orange);
    transform: rotate(-9deg);
    display: flex; align-items: center; justify-content: center;
    color: var(--white);
    font-family: "Fira Sans Condensed", sans-serif;
    font-weight: 700; font-size: 42px; letter-spacing: 0.5px;
  }
  .voucher-tag sup { font-size: 22px; margin-right: 2px; }

  .headline {
    position: absolute; left: 0; top: 356px; width: 846px;
    text-align: center;
    font-family: "Montserrat", sans-serif; font-weight: 800;
    margin: 0; line-height: 1;
  }
  .headline-top { display: block; color: var(--brown); font-size: 62px; }
  .headline-bottom { display: block; color: var(--orange); font-size: 64px; margin-top: 20px; }

  .offer-panel {
    position: absolute; left: 75px; top: 528px;
    width: 695px; height: 332px;
    background: linear-gradient(160deg, var(--yellow-light) 0%, var(--yellow-deep) 100%);
    box-shadow: 0 10px 14px rgba(0,0,0,0.25);
    text-align: center;
  }
  .offer-script {
    margin: 14px 0 0;
    font-family: "Oleo Script", cursive; font-weight: 700;
    color: var(--brown); font-size: 60px; line-height: 1.1;
  }
  .offer-team {
    margin: 8px 0 0;
    font-family: "Fira Sans Condensed", sans-serif; font-weight: 700;
    color: var(--teal); font-size: 37px; letter-spacing: 1.5px;
  }
  .dotted-rule {
    width: 464px; margin: 12px auto 0;
    border-top: 5px dotted var(--brown);
  }
  .offer-body {
    margin: 10px 0 10px;
    color: var(--brown); font-size: 27px; line-height: 40px;
  }
  .offer-body sup { font-size: 15px; }

  .terms {
    position: absolute; left: 0; top: 890px; width: 846px;
    text-align: center; margin: 0;
    font-family: "PT Sans Narrow", sans-serif; font-weight: 700;
    color: var(--ink); font-size: 21px; line-height: 30px;
  }

  .clinic-name {
    position: absolute; left: 138px; top: 986px;
    width: 238px; height: 110px;
    display: flex; align-items: center; gap: 14px;
  }
  .clinic-dot { width: 36px; height: 36px; border-radius: 50%; background: var(--orange); flex: none; }
  .clinic-text { color: var(--brown); font-weight: 700; font-size: 27px; line-height: 34px; }

  .services {
    position: absolute; left: 418px; top: 980px;
    margin: 0; padding: 0; list-style: none;
    font-family: "Roboto Slab", serif; font-weight: 500;
    color: var(--brown); font-size: 21px; letter-spacing: 0.5px;
  }
  .services li { display: flex; align-items: center; height: 30px; }
  .services li::before {
    content: ""; width: 12px; height: 12px; border-radius: 50%;
    background: var(--brown); margin-right: 14px;
  }

  .contact-bar {
    position: absolute; left: 0; top: 1138px;
    width: 846px; height: 62px;
    background: var(--orange-deep);
    display: flex; align-items: center; justify-content: center; gap: 12px;
    color: var(--white);
    font-family: "Fira Sans Condensed", sans-serif; font-weight: 700; font-size: 31px;
  }
  .contact-divider { margin: 0 4px; }
</style>
</head>
<body>
<main class="poster">
  <div class="hero-photo" role="img" aria-label="Photo of a golden puppy nuzzling a grey kitten against a white background"></div>
  <svg class="torn-edge" width="846" height="70" viewBox="0 0 846 70" aria-hidden="true">
    <polygon fill="#f3f1ec" points="0,32 40,22 80,28 120,12 170,20 215,4 260,16 300,10 350,24 395,8 440,18 490,6 520,16 560,28 610,34 660,24 700,30 745,18 790,26 846,14 846,70 0,70"/>
  </svg>

  <div class="voucher-badge">
    <div class="voucher-frame"></div>
    <div class="voucher-tag"><sup>$</sup>30 VOUCHER</div>
  </div>

  <h1 class="headline">
    <span class="headline-top">WE LOVE</span>
    <span class="headline-bottom">TAIL TELLERS!</span>
  </h1>

  <section class="offer-panel">
    <p class="offer-script">Refer a fur friend</p>
    <p class="offer-team">TO OUR FRIENDLY TEAM</p>
    <div class="dotted-rule"></div>
    <p class="offer-body">and both your fur child and<br>their fur child will receive a<br><sup>$</sup>30 voucher to use in clinic! *</p>
    <div class="dotted-rule"></div>
  </section>

  <p class="terms">* Limited to one pet per fur parent and the referred fur parent must be<br>new to our clinic. Unlimited vouchers for number of referrals!</p>

  <div class="clinic-name">
    <span class="clinic-dot"></span>
    <span class="clinic-text">Mossbury Vet<br>Kelvale</span>
  </div>

  <ul class="services">
    <li>PREVENTIVE CARE</li>
    <li>DIAGNOSTICS</li>
    <li>SURGERY</li>
    <li>BEHAVIOR &amp; TRAINING</li>
  </ul>

  <footer class="contact-bar">
    <svg width="28" height="28" viewBox="0 0 28 28" aria-hidden="true">
      <circle cx="14" cy="14" r="12.5" fill="none" stroke="#fff" stroke-width="2"/>
      <path d="M10 8 l3 0 l1 4 l-2 1.5 q1.5 3 4 4.5 l1.5 -2 l4 1 l0 3 q-8 0 -11.5 -12z" fill="#fff"/>
    </svg>
    <span>(02) 5550 1847</span><span class="contact-divider">|</span><span>www.mossbury-vet.com.au</span>
  </footer>
</main>
</body>
</html>
```